Business card for consulting firm

We need a double-sided business card for consulting firm, VantorQ. The card should be professional but also creative and visually interesting.

Target Market(s)

Engineering and technology; transport industries; safety critical / heavy industry.

Contact Information for Business Card

See attached file with details.

Font styles to use
Sans Serif

```html
<!DOCTYPE html>
<html lang="en">
<head>
<meta charset="utf-8">
<title>VantorQ Business Card</title>
<link href="https://fonts.googleapis.com/css2?family=Montserrat:ital,wght@0,400;0,500;0,600;1,500&display=swap" rel="stylesheet">
<style>
  :root {
    --page-bg: #c9c9c9;
    --navy-deep: #05202f;
    --teal-mid: #0e4f6a;
    --teal-light: #1a7c9d;
    --accent-blue: #2aa6db;
    --ink: #13243a;
    --ink-soft: #2a3546;
    --card-white: #f3f4f4;
    --card-white-edge: #e7e8e9;
    --pattern-tint: rgba(170, 205, 222, 0.45);
    --on-dark: #f1f4f6;
  }
  * { box-sizing: border-box; margin: 0; padding: 0; }
  html, body {
    width: 1200px;
    height: 576px;
    overflow: hidden;
  }
  body {
    background: var(--page-bg);
    font-family: "Montserrat", sans-serif;
    position: relative;
  }
  .card {
    position: absolute;
    top: 138px;
    width: 484px;
    height: 294px;
    border-radius: 16px;
    overflow: hidden;
    box-shadow: 0 3px 8px rgba(0, 0, 0, 0.22);
  }
  .card--front {
    left: 82px;
    background: linear-gradient(180deg, var(--navy-deep) 0%, var(--teal-mid) 50%, var(--teal-light) 100%);
  }
  .card--back {
    left: 602px;
    background: linear-gradient(180deg, var(--card-white) 0%, var(--card-white-edge) 100%);
  }
  .front-texture {
    position: absolute;
    inset: 0;
    background:
      radial-gradient(ellipse at 30% 35%, rgba(255,255,255,0.06), transparent 60%),
      radial-gradient(ellipse at 75% 70%, rgba(255,255,255,0.05), transparent 55%);
  }
  .wordmark {
    position: absolute;
    font-weight: 600;
    letter-spacing: 0.04em;
    white-space: nowrap;
    line-height: 1;
  }
  .card--front .wordmark {
    left: 0;
    right: 0;
    top: 136px;
    text-align: center;
    font-size: 40px;
    color: var(--on-dark);
  }
  .front-url {
    position: absolute;
    left: 0;
    right: 0;
    top: 266px;
    text-align: center;
    font-size: 13px;
    color: var(--on-dark);
    opacity: 0.9;
  }
  .back-texture {
    position: absolute;
    right: -30px;
    bottom: -40px;
    width: 260px;
    height: 200px;
    background: radial-gradient(ellipse at 55% 55%, var(--pattern-tint) 0%, rgba(170,205,222,0.15) 55%, transparent 75%);
  }
  .card--back .wordmark {
    left: 31px;
    top: 142px;
    font-size: 33px;
    color: var(--ink);
  }
  .holder {
    position: absolute;
    left: 260px;
    top: 78px;
  }
  .holder__name {
    font-size: 19px;
    font-weight: 500;
    color: var(--ink);
    line-height: 1.1;
  }
  .holder__credentials {
    font-size: 9.5px;
    color: var(--ink-soft);
    margin-top: 3px;
  }
  .holder__role {
    font-size: 12px;
    font-style: italic;
    font-weight: 500;
    color: var(--accent-blue);
    margin-top: 5px;
  }
  .contacts {
    position: absolute;
    left: 263px;
    top: 148px;
    list-style: none;
  }
  .contacts__item {
    display: flex;
    align-items: center;
    height: 16.5px;
    font-size: 12px;
    color: var(--ink);
  }
  .contacts__icon {
    width: 10px;
    height: 10px;
    margin-right: 6px;
    flex: none;
  }
</style>
</head>
<body>

  <section class="card card--front">
    <div class="front-texture" role="img" aria-label="Decorative pattern of soft overlapping rounded shapes in deep teal"></div>
    <div class="wordmark">VANTORQ</div>
    <div class="front-url">www.vantorq.com.au</div>
  </section>

  <section class="card card--back">
    <div class="back-texture" role="img" aria-label="Faint decorative pattern of pale blue rounded shapes"></div>
    <div class="wordmark">VANTORQ</div>

    <div class="holder">
      <div class="holder__name">Maren Holloway</div>
      <div class="holder__credentials">BA (Hons), M Psych Org, M Tech Mgt (HF)</div>
      <div class="holder__role">Managing Director</div>
    </div>

    <ul class="contacts">
      <li class="contacts__item">
        <svg class="contacts__icon" viewBox="0 0 10 10" aria-hidden="true">
          <circle cx="5" cy="5" r="4.4" fill="none" stroke="#2aa6db" stroke-width="1"/>
          <path d="M3.4 2.8 L4.2 2.6 L4.6 3.8 L4.1 4.2 Q4.6 5.3 5.8 5.9 L6.2 5.4 L7.3 5.8 L7.1 6.6 Q5.4 7 3.9 5.5 Q3 4.3 3.4 2.8 Z" fill="#2aa6db"/>
        </svg>
        +61 (0)400 555 018
      </li>
      <li class="contacts__item">
        <svg class="contacts__icon" viewBox="0 0 10 10" aria-hidden="true">
          <rect x="0.7" y="2" width="8.6" height="6" fill="none" stroke="#2aa6db" stroke-width="1"/>
          <path d="M0.7 2 L5 5.5 L9.3 2" fill="none" stroke="#2aa6db" stroke-width="1"/>
        </svg>
        mholloway@vantorq.com.au
      </li>
      <li class="contacts__item">
        <svg class="contacts__icon" viewBox="0 0 10 10" aria-hidden="true">
          <circle cx="5" cy="5" r="4.5" fill="#2aa6db"/>
          <path d="M0.5 5 H9.5 M5 0.5 Q2.5 5 5 9.5 M5 0.5 Q7.5 5 5 9.5" fill="none" stroke="#f3f4f4" stroke-width="0.7"/>
        </svg>
        www.vantorq.global
      </li>
      <li class="contacts__item">
        <svg class="contacts__icon" viewBox="0 0 10 10" aria-hidden="true">
          <circle cx="5" cy="5" r="4.5" fill="#2aa6db"/>
          <path d="M0.5 5 H9.5 M5 0.5 Q2.5 5 5 9.5 M5 0.5 Q7.5 5 5 9.5" fill="none" stroke="#f3f4f4" stroke-width="0.7"/>
        </svg>
        www.vantorq.com.au
      </li>
    </ul>
  </section>

</body>
</html>
```